a residential painting contractor I need a 6x9 postcard made

I already have a logo, I'm trying to offer my services to people. you can put that there's a 250$ discount for first time customers. include my License number #4627381 as well as the services I offer, interior and exterior painting, pressure washing, cabinet painting, epoxy floors, wood staining, decks, fences and much more. I'm licensed bonded and insured as well.

Target Market(s)

residential consumers (homeowners)

Industry/Entity Type

Painting contractor

Requirements
Must have
• postage stuff on the back I've linked some pictures top right please, my license number, what I do, phone number (555)317-0846 email velbrushworks7@mailzo.net, front and back of postcard
Nice to have
• well lit house in the background, maybe little circles of people doing some of the services I offer

```html
<!DOCTYPE html>
<html lang="en">
<head>
<meta charset="utf-8">
<title>Velbrush Works Postcard</title>
<link href="https://fonts.googleapis.com/css2?family=Oswald:wght@300;500;600&family=Libre+Baskerville:ital,wght@0,700;1,400;1,700&family=Raleway:wght@500&family=Montserrat:wght@700&display=swap" rel="stylesheet">
<style>
:root{
  --stage:#8a8a8a;
  --ink:#1b1b1b;
  --white:#ffffff;
  --sky:#7fcdee;
  --sky-top:#a9d8f9;
  --sky-bottom:#eef8fe;
  --muted:#d9d9d9;
}
*{margin:0;padding:0;box-sizing:border-box}
html,body{width:960px;height:1200px;overflow:hidden;background:var(--stage)}
.card{position:absolute;width:648px;height:431px;overflow:hidden}
.front{left:156px;top:130px}
.back{left:170px;top:624px;background:linear-gradient(180deg,var(--sky-top),var(--sky-bottom) 55%)}
.photo{position:absolute}
.front-scene{inset:0;background:linear-gradient(180deg,#6f7fa0 0%,#4d5a78 35%,#8a7a5e 62%,#4f7a3a 80%,#3b5e2c 100%)}
.painter{left:473px;top:37px;width:175px;height:300px;background:linear-gradient(180deg,#5ab8e4 0%,#62c2ec 45%,#f2f2f2 55%,#e8e8e8 100%);border-radius:60px 60px 0 0}
.wave{position:absolute;left:0;top:0;width:648px;height:431px}
.brand-banner{position:absolute;left:51px;top:0;width:152px;height:172px;background:var(--white);display:flex;align-items:center;justify-content:center;clip-path:polygon(0 0,100% 0,100% 100%,50% 96%,0 100%)}
.brand-name{font-family:'Oswald',sans-serif;font-weight:600;color:var(--ink);text-transform:uppercase;text-align:center;line-height:1.05}
.brand-banner .brand-name{font-size:22px}
.burst{position:absolute;left:393px;top:192px;width:180px;height:180px}
.burst-text{position:absolute;left:393px;top:192px;width:180px;height:180px;display:flex;flex-direction:column;align-items:center;justify-content:center;color:var(--ink);text-align:center}
.price{font-family:'Libre Baskerville',serif;font-weight:700;font-size:46px;line-height:1}
.price sup{font-size:22px;vertical-align:4px}
.discount{font-family:'Libre Baskerville',serif;font-weight:700;font-size:19px;line-height:1.1}
.first-time{font-family:'Oswald',sans-serif;font-weight:500;font-size:18px;line-height:1;margin-top:4px}
.front-contact{position:absolute;left:54px;width:260px;text-align:center;color:var(--white)}
.call{font-family:'Oswald',sans-serif;font-weight:600;font-size:34px;line-height:1}
.phone{font-family:'Oswald',sans-serif;font-weight:600;font-size:36px;line-height:1}
.front .call{top:311px}
.front .phone{top:347px}
.front .email{position:absolute;left:54px;top:389px;width:260px;text-align:center;font-family:'Libre Baskerville',serif;font-weight:700;font-size:11.5px;color:var(--white)}
.credentials{position:absolute;left:368px;top:389px;font-family:'Raleway',sans-serif;font-weight:500;font-size:15px;color:var(--muted)}
.tile{position:absolute;width:103px;height:92px;border-radius:4px}
.label{position:absolute;width:125px;text-align:center;font-family:'Oswald',sans-serif;font-weight:500;font-size:9.5px;line-height:1.1;color:var(--ink)}
.postal{position:absolute;background:var(--white);border:1px solid var(--ink);font-family:'Montserrat',sans-serif;font-weight:700;color:var(--ink)}
.postal-customer{left:398px;top:26px;width:119px;height:29px;font-size:7.5px;line-height:1.3;padding:4px 8px}
.postal-permit{left:530px;top:23px;width:90px;height:67px;font-size:9.5px;line-height:1.25;text-align:center;padding-top:2px}
.back-house{left:0;top:233px;width:381px;height:198px;background:linear-gradient(180deg,#cfe6f3 0%,#8a8d8a 35%,#6d6a62 60%,#4f8a3a 85%,#5ba23e 100%)}
.back-band{position:absolute;left:0;top:0;width:648px;height:431px}
.seal{position:absolute;left:494px;top:135px;width:140px;height:140px;border-radius:50%;background:var(--white);display:flex;align-items:center;justify-content:center}
.seal .brand-name{font-size:20px}
.back-contact{position:absolute;right:24px;text-align:right;color:var(--white)}
.back .call{top:290px;right:27px}
.back .phone{top:328px;right:23px}
.back .email{top:365px;right:29px;font-family:'Oswald',sans-serif;font-weight:300;font-size:18px}
.license{top:393px;right:29px;font-family:'Libre Baskerville',serif;font-style:italic;font-size:13.5px}
.license b{font-weight:700}
</style>
</head>
<body>

<section class="card front">
  <div class="photo front-scene" role="img" aria-label="Well-lit craftsman house with porch at dusk, trees and lawn"></div>
  <div class="photo painter" role="img" aria-label="Smiling painter in cap and white overalls holding a paint roller"></div>
  <svg class="wave" viewBox="0 0 648 431" aria-hidden="true">
    <path d="M0 431 L0 300 C6 318 14 332 30 330 C140 305 300 282 430 298 C530 310 610 330 640 310 L648 296 L648 431 Z" fill="#1b1b1b"/>
  </svg>
  <div class="brand-banner"><span class="brand-name">Velbrush<br>Works</span></div>
  <svg class="burst" viewBox="0 0 180 180" aria-hidden="true">
    <g fill="#7fcdee" transform="translate(90 90)">
      <rect x="-66" y="-66" width="132" height="132"/>
      <rect x="-66" y="-66" width="132" height="132" transform="rotate(22.5)"/>
      <rect x="-66" y="-66" width="132" height="132" transform="rotate(45)"/>
      <rect x="-66" y="-66" width="132" height="132" transform="rotate(67.5)"/>
    </g>
  </svg>
  <div class="burst-text">
    <div class="price"><sup>$</sup>250</div>
    <div class="discount">DISCOUNT</div>
    <div class="first-time">FIRST TIME<br>CUSTOMERS</div>
  </div>
  <div class="front-contact call">CALL US</div>
  <div class="front-contact phone">(555) 317-0846</div>
  <div class="email">VELBRUSHWORKS7@MAILZO.NET</div>
  <div class="credentials">LICENSED, BONDED &amp; INSURED</div>
</section>

<section class="card back">
  <div class="tile" style="left:23px;top:11px;background:linear-gradient(135deg,#f1eee6,#9aa4ad)" role="img" aria-label="Worker in hard hat rolling paint on a wall"></div>
  <div class="tile" style="left:139px;top:11px;background:linear-gradient(180deg,#5d9a3e,#b9443a)" role="img" aria-label="Worker pressure washing a tiled roof"></div>
  <div class="tile" style="left:257px;top:11px;background:linear-gradient(135deg,#f4f4f2,#cfd2d0)" role="img" aria-label="Brush painting a white cabinet door"></div>
  <div class="label" style="left:12px;top:103px">INTERIOR &amp; EXTERIOR<br>PAINTING</div>
  <div class="label" style="left:128px;top:104px">PRESSURE WASHING</div>
  <div class="label" style="left:246px;top:107px">CABINET PAINTING</div>

  <div class="tile" style="left:23px;top:128px;background:linear-gradient(135deg,#8fa6b8,#6d8598)" role="img" aria-label="Worker spreading epoxy coating on a floor"></div>
  <div class="tile" style="left:139px;top:128px;background:linear-gradient(135deg,#e7c39a,#b9835a)" role="img" aria-label="Hand staining wood planks with a brush"></div>
  <div class="tile" style="left:257px;top:128px;background:linear-gradient(135deg,#8f8578,#6a6258)" role="img" aria-label="Finished composite deck boards with plants"></div>
  <div class="tile" style="left:375px;top:128px;background:linear-gradient(180deg,#cfe3ef,#4f8a3a 55%,#6aa845)" role="img" aria-label="White rail fence on green lawn"></div>
  <div class="label" style="left:12px;top:223px">EPOXY FLOORS</div>
  <div class="label" style="left:128px;top:223px">WOOD STAINING</div>
  <div class="label" style="left:246px;top:223px">DECKS</div>
  <div class="label" style="left:364px;top:223px">FENCES</div>

  <div class="postal postal-customer">LOCAL POSTAL<br>CUSTOMER</div>
  <div class="postal postal-permit">PRSRT STD<br>ECRWSS<br>U.S.POSTAGE<br><span style="font-size:11.5px">PAID</span><br>EDDM Retail</div>

  <div class="photo back-house" role="img" aria-label="Large two-story gray house with landscaped front yard"></div>
  <svg class="back-band" viewBox="0 0 648 431" aria-hidden="true">
    <path d="M270 431 C360 380 440 320 510 240 C570 170 615 110 648 48 L648 431 Z" fill="#1b1b1b"/>
  </svg>
  <div class="seal"><span class="brand-name">Velbrush<br>Works</span></div>

  <div class="back-contact call">CALL US</div>
  <div class="back-contact phone">(555)317-0846</div>
  <div class="back-contact email">VELBRUSHWORKS7@MAILZO.NET</div>
  <div class="back-contact license">License number <b>#4627381</b></div>
</section>

</body>
</html>
```